2 business magazine ads

Ad 1 — Kestrelview Aero LLC

Ad Type: Full Page | 8.5” × 11” + ¼” Bleed
Audience: Builders • Developers • Contractors
Goal: Promote drone-based visual and thermal services for construction and land development.

Headline Options
• See Every Angle. Build with Precision.
• Your Job Site, Elevated.
• Thermal Inspection. Progress Tracking. Mapping Mastery.

Body Copy

Kestrelview Aero LLC provides professional UAS services to builders and developers across Georgia — delivering the clarity, accuracy, and efficiency your projects demand.

• Thermal Inspections – Detect moisture intrusion, heat loss, and electrical issues early.
• Construction Progress Tracking – Aerial documentation from foundation to finish.
• Land Mapping & Survey Support – Orthomosaic mapping, elevation models, and site analytics.

Certified & Compliant: FAA Licensed • NDPCA Level III • Level 1 Thermographer • OSHA 10 Certified

Call to Action

KestrelviewAero.com | (706) ###-#### | Follow @KestrelviewAero

Design Notes
• Visual: crisp aerial of active construction site with thermal overlay or orthomosaic grid.
• Include FAA and certification badges along the bottom bar.
• Clean, modern layout with bold logo and a “technical blue + white” color palette.

Ad 2 — T&M Assurance Partners LLC

Audience: High-Net-Worth Homeowners • Luxury Builders • Contractors
Goal: Showcase boutique-level insurance expertise for property and construction clients.

Headline Options
• Protect What You’ve Built — and What Builds You.
• Boutique Coverage for Extraordinary Homes & Businesses.
• Luxury Homes. Smart Builders. Sound Protection.

Body Copy

T&M Assurance Partners LLC provides custom-tailored coverage for those who build, own, and protect extraordinary properties.

• High-Value Homes & HNW Client Coverage
• Builders Risk & Contractors Liability
• Business Auto • Workers Comp • Property Protection

As an independent boutique agency, we deliver personal service and deep expertise backed by trusted national carriers — helping you secure the future you’ve built.

Call to Action

T&MAssurancePartners.com | Ashmoor, GA | (706) ###-####

Design Notes
• Visual: luxury home or builder blueprint composite image.
• Tone: refined and trustworthy — navy, white, and gold palette.
• Layout: prominent logo at top or bottom, clean copy zones with ample white space.

Target Market(s)

Luxury home contractors

Industry/Entity Type

Drone thermal inspection and construction progress tracking, HNW insurance provider, Contractor insurance coverage

Requirements
Must have
• kestrelview - vexo altura 7k drone, luxury lake home under construction. T&M - should show luxury lake home in photo ie lake wendabee in Ashmoor, GA 30719

```html
<!DOCTYPE html>
<html lang="en">
<head>
<meta charset="utf-8">
<title>T&amp;M Assurance Partners — Full Page Ad</title>
<link rel="stylesheet" href="https://fonts.googleapis.com/css2?family=DM+Sans:wght@400;500&family=DM+Serif+Display&family=DM+Serif+Text:ital@1&display=swap">
<style>
  :root {
    --backdrop: #3d3d3f;
    --navy: #0f1338;
    --ink: #1a1a24;
    --gold: #c99a3e;
    --gold-light: #f3d58c;
    --gold-deep: #a87426;
    --copy-gold: #b27c2c;
    --white: #ffffff;
    --sky-top: #5f7597;
    --sky-mid: #9fb0c9;
    --glow: #e9c3a4;
  }
  * { box-sizing: border-box; margin: 0; padding: 0; }
  html, body { width: 1041px; height: 1200px; overflow: hidden; }
  body { background: var(--backdrop); position: relative; font-family: "DM Sans", sans-serif; }

  .ad {
    position: absolute; left: 126px; top: 99px;
    width: 767px; height: 992px;
    background: var(--white); overflow: hidden;
  }
  .hero-photo {
    position: absolute; inset: 0 0 auto 0; height: 640px;
    background:
      radial-gradient(ellipse 45% 25% at 80% 62%, rgba(240,200,170,.75), transparent 70%),
      linear-gradient(90deg, rgba(35,40,55,.85) 0%, rgba(80,70,70,.55) 28%, rgba(120,110,120,.15) 55%, transparent 70%),
      linear-gradient(180deg, var(--sky-top) 0%, var(--sky-mid) 45%, var(--glow) 70%, var(--white) 100%);
  }
  .hero-fade {
    position: absolute; left: 0; right: 0; top: 470px; height: 190px;
    background: linear-gradient(180deg, rgba(255,255,255,0), #fff 85%);
  }

  .wordmark {
    position: absolute; left: 0; right: 0; top: 90px;
    display: flex; align-items: center; justify-content: center; gap: 10px;
    color: var(--white); font-size: 24px; font-weight: 500; line-height: 30px;
  }
  .wordmark-dot { width: 14px; height: 14px; border-radius: 50%; background: var(--gold); }

  .headline { position: absolute; left: 0; right: 0; top: 190px; text-align: center; color: var(--white);
    font-family: "DM Serif Display", serif; font-weight: 400; text-shadow: 0 2px 8px rgba(0,0,0,.25); }
  .headline .line-1 { display: block; font-size: 35px; line-height: 46px; }
  .headline .line-2 { display: block; font-size: 58px; line-height: 60px; }

  .intro { position: absolute; left: 0; right: 0; top: 551px; text-align: center;
    font-size: 18.5px; line-height: 24.5px; color: var(--ink); }

  .service { position: absolute; top: 627px; width: 150px; text-align: center;
    font-size: 17px; line-height: 21px; color: var(--ink); }
  .service-badge { width: 94px; height: 94px; margin: 0 auto 8px; border-radius: 50%;
    background: radial-gradient(circle at 40% 35%, var(--gold-light), var(--gold) 55%, var(--gold-deep));
    box-shadow: 0 3px 8px rgba(120,80,20,.25);
    display: flex; align-items: center; justify-content: center; }
  .service-badge svg { width: 52px; height: 52px; fill: none; stroke: var(--navy); stroke-width: 2.2; stroke-linejoin: round; stroke-linecap: round; }
  .service-homes { left: 50px; }
  .service-auto { left: 183px; }
  .service-builders { left: 316px; }
  .service-workers { left: 454px; }
  .service-property { left: 591px; }

  .promise { position: absolute; left: 0; right: 0; top: 815px; text-align: center;
    font-family: "DM Serif Text", serif; font-style: italic; font-size: 16.5px; line-height: 21px; color: var(--copy-gold); }

  .footer-band { position: absolute; left: 0; top: 900px; width: 767px; height: 92px; }
  .contact-bar { position: absolute; left: 0; right: 0; bottom: 0; height: 70px;
    display: flex; align-items: center; justify-content: center; color: var(--white); font-size: 17.5px; }
  .contact-item { display: flex; align-items: center; gap: 9px; padding: 0 20px; }
  .contact-item svg { width: 20px; height: 20px; fill: none; stroke: var(--gold); stroke-width: 1.8; }
  .divider { width: 1px; height: 34px; background: rgba(255,255,255,.6); }
</style>
</head>
<body>
  <main class="ad">
    <div class="hero-photo" role="img" aria-label="Modern luxury lake home with glass walls and a palm tree under a dusk sky"></div>
    <div class="hero-fade"></div>

    <div class="wordmark"><span class="wordmark-dot"></span>T&amp;M Assurance Partners</div>

    <h1 class="headline">
      <span class="line-1">Protect What You’ve Built</span>
      <span class="line-2">and What Builds You</span>
    </h1>

    <p class="intro">T&amp;M Assurance Partners LLC provides custom-tailored coverage for<br>those who build, own, and protect extraordinary properties.</p>

    <section class="services">
      <div class="service service-homes">
        <div class="service-badge"><svg viewBox="0 0 48 48"><path d="M8 42V18h10v24M18 42V12h12v30M30 42V20h10v22M4 42h40M12 23h2M12 29h2M12 35h2M22 17h4M22 23h4M22 29h4M22 35h4M34 25h2M34 31h2M34 37h2M16 6l1 2 2 .3-1.5 1.4.4 2.1L16 11l-1.9 1 .4-2.1L13 8.3l2-.3zM32 6l1 2 2 .3-1.5 1.4.4 2.1L32 11l-1.9 1 .4-2.1L29 8.3l2-.3z"/></svg></div>
        High-Value<br>Homes &amp; HNW<br>Client Coverage
      </div>
      <div class="service service-auto">
        <div class="service-badge"><svg viewBox="0 0 48 48"><circle cx="24" cy="14" r="6"/><path d="M14 30c1-6 5-9 10-9s9 3 10 9M6 30l8 6 6-4 6 4M42 30l-8 6-8-6M20 36l4 4 4-4"/></svg></div>
        Business<br>Auto
      </div>
      <div class="service service-builders">
        <div class="service-badge"><svg viewBox="0 0 48 48"><path d="M8 26h28M10 26c0-8 5-13 12-13s12 5 12 13M22 13v-3M14 30a8 8 0 0 0 16 0M36 6l8 14H28z M36 11v4M36 17v.5"/><circle cx="22" cy="31" r="3"/></svg></div>
        Builders Risk<br>&amp; Contractors<br>Liability
      </div>
      <div class="service service-workers">
        <div class="service-badge"><svg viewBox="0 0 48 48"><circle cx="24" cy="15" r="5"/><path d="M18 12c0-4 3-6 6-6s6 2 6 6M14 42V32c0-5 4-9 10-9s10 4 10 9v10"/><circle cx="10" cy="22" r="4"/><circle cx="38" cy="22" r="4"/><path d="M3 40v-6c0-3 3-6 7-6M45 40v-6c0-3-3-6-7-6M24 23l-3 8 3 4 3-4z"/></svg></div>
        Workers<br>Comp
      </div>
      <div class="service service-property">
        <div class="service-badge"><svg viewBox="0 0 48 48"><path d="M4 42h40M28 42V12h12v30M31 17h2M35 17h2M31 23h2M35 23h2M31 29h2M35 29h2M31 8h6v4M14 10l-10 4v8c0 7 4 12 10 14 6-2 10-7 10-14v-8z M9 22l4 4 6-7"/></svg></div>
        Property<br>Protection
      </div>
    </section>

    <p class="promise">As an independent boutique agency, we deliver personal service and deep expertise backed<br>by trusted national carriers — helping you secure the future you’ve built.</p>

    <svg class="footer-band" viewBox="0 0 767 92" preserveAspectRatio="none" aria-hidden="true">
      <defs>
        <linearGradient id="goldRule" x1="0" x2="1">
          <stop offset="0" stop-color="#b8862f"/><stop offset=".5" stop-color="#f6dc98"/><stop offset="1" stop-color="#b8862f"/>
        </linearGradient>
      </defs>
      <path d="M0 38 Q383 -20 767 38 L767 92 L0 92Z" fill="url(#goldRule)"/>
      <path d="M0 45 Q383 -12 767 45 L767 92 L0 92Z" fill="#0f1338"/>
    </svg>

    <footer class="contact-bar">
      <span class="contact-item">
        <svg viewBox="0 0 24 24"><circle cx="12" cy="12" r="10"/><ellipse cx="12" cy="12" rx="4.5" ry="10"/><path d="M2 12h20M4 7h16M4 17h16"/></svg>
        T&amp;MAssurancePartners.com
      </span>
      <span class="divider"></span>
      <span class="contact-item">
        <svg viewBox="0 0 24 24"><path d="M6 3l3 5-2 2c1 3 3 5 6 6l2-2 5 3-2 4C10 20 4 14 3 5z" fill="#c99a3e" stroke="none"/></svg>
        706-555-0148
      </span>
      <span class="divider"></span>
      <span class="contact-item">
        <svg viewBox="0 0 24 24"><path d="M12 22s7-7 7-12a7 7 0 0 0-14 0c0 5 7 12 7 12z"/><circle cx="12" cy="10" r="2.5"/></svg>
        Ashmoor, GA
      </span>
    </footer>
  </main>
</body>
</html>
```